Screening Mammography flyer for patients

We need a flyer design to inform our patients of our Screening Mammography program (it's a screening Diagnostic Imaging test). Women aged 50-74 years old are eligible for this exam. We also have a convenient booking system, when a patient can call us directly. There's no doctor’s referral needed to sign up for the test.
We are also starting the TLR Scanwell Envoy program, when select patients will help spread the word and save lives.
The flyer has to be done with a lot of pink color as it is a traditional color for Breast cancer materials, with consideration of the hospital's corporate colors (the brand book is attached).

Diagnostic Imaging

```html
<!DOCTYPE html>
<html lang="en">
<head>
<meta charset="utf-8">
<title>Screening Mammography Flyer</title>
<link href="https://fonts.googleapis.com/css2?family=Jost:wght@400;500;700;800&display=swap" rel="stylesheet">
<style>
  :root {
    --pink: #e0147f;
    --pink-light: #f05aa6;
    --pink-soft: #f7c4dc;
    --green: #7dbb2f;
    --green-dark: #5f9a1e;
    --ink: #474747;
    --white: #ffffff;
    --stage: #2a2a2a;
  }
  html, body {
    margin: 0;
    padding: 0;
    width: 1200px;
    height: 960px;
    overflow: hidden;
    background: var(--stage);
  }
  .flyer {
    position: absolute;
    left: 30px;
    top: 76px;
    width: 1140px;
    height: 807px;
    font-family: "Jost", "Futura", sans-serif;
  }
  .flyer svg { display: block; width: 100%; height: 100%; }
  .headline { font-weight: 800; fill: var(--pink); }
  .subhead { font-weight: 400; fill: var(--ink); }
  .subhead-strong { font-weight: 700; }
  .accent { fill: var(--pink); font-weight: 700; }
  .brand-name { font-weight: 700; fill: var(--green-dark); letter-spacing: 1.5px; }
  .band-text { fill: var(--white); font-weight: 400; }
  .band-strong { font-weight: 700; }
  .cta-text { fill: var(--pink); font-weight: 400; }
  .cta-strong { font-weight: 700; }
  .badge-text { fill: var(--pink); font-weight: 800; }
  .badge-small { fill: var(--pink); font-weight: 700; }
  .footer-text { fill: var(--white); font-weight: 400; }
</style>
</head>
<body>
<div class="flyer">
  <svg viewBox="0 0 1290 913" xmlns="http://www.w3.org/2000/svg">
    <defs>
      <linearGradient id="photoTone" x1="0" y1="0" x2="1" y2="0">
        <stop offset="0" stop-color="#6e5a40"/>
        <stop offset="0.16" stop-color="#b0708e"/>
        <stop offset="0.36" stop-color="#b9c56c"/>
        <stop offset="0.56" stop-color="#e8eec8"/>
        <stop offset="0.76" stop-color="#fbfaf2"/>
        <stop offset="1" stop-color="#ffffff"/>
      </linearGradient>
      <linearGradient id="waveTone" x1="0" y1="0" x2="0" y2="1">
        <stop offset="0" stop-color="var(--pink-light)"/>
        <stop offset="1" stop-color="var(--pink)"/>
      </linearGradient>
      <radialGradient id="ribbonTone" cx="0.3" cy="0.65" r="0.7">
        <stop offset="0" stop-color="var(--pink-soft)" stop-opacity="0.9"/>
        <stop offset="1" stop-color="var(--pink-soft)" stop-opacity="0"/>
      </radialGradient>
      <clipPath id="badgeInner">
        <circle cx="1100" cy="560" r="98"/>
      </clipPath>
    </defs>

    <!-- background photo area -->
    <rect class="photo" role="img" aria-label="Photo of a woman in a pink plaid shirt reading a book against a tree in a sunny park" x="0" y="0" width="1290" height="913" fill="url(#photoTone)"/>

    <!-- brand lockup -->
    <rect x="1040" y="62" width="52" height="52" fill="var(--green)"/>
    <text class="brand-name" font-size="24">
      <tspan x="1112" y="69">TALLOW</tspan>
      <tspan x="1112" y="95">RIDGE</tspan>
      <tspan x="1112" y="121">HOSPITAL</tspan>
    </text>
    <line x1="895" y1="131" x2="1251" y2="131" stroke="var(--green)" stroke-width="2"/>
    <text class="brand-name" font-size="16.5" x="895" y="158" textLength="356" lengthAdjust="spacing">LAKESHORE EAST HEALTH NETWORK</text>

    <!-- headline -->
    <text class="headline" font-size="97" x="1251" y="268" text-anchor="end">JUST BOOK IT</text>
    <text class="subhead" font-size="55" x="573" y="330" textLength="678" lengthAdjust="spacing">FOR WOMEN <tspan class="subhead-strong">AGED 50-74</tspan></text>
    <text class="subhead" font-size="38" x="573" y="385" textLength="678" lengthAdjust="spacing"><tspan class="accent">JOIN</tspan> THE TLR SCANWELL ENVOY</text>
    <text class="subhead" font-size="38" x="715" y="425" textLength="536" lengthAdjust="spacing">PROGRAM TO HELP SAVE LIVES!</text>

    <!-- pink wave band -->
    <path d="M0 615 C 220 540, 450 500, 645 500 C 880 500, 1100 540, 1290 635 L1290 913 L0 913 Z" fill="var(--green)"/>
    <path d="M0 624 C 220 550, 450 510, 645 510 C 880 510, 1100 550, 1290 647 L1290 913 L0 913 Z" fill="url(#waveTone)"/>
    <path d="M0 678 C 400 662, 900 662, 1290 678 L1290 913 L0 913 Z" fill="var(--pink)"/>

    <text class="band-text" font-size="45" x="250" y="617" textLength="688" lengthAdjust="spacing">NO DOCTOR’S REFERRAL NEEDED</text>
    <text class="band-text" font-size="45" x="200" y="667" textLength="788" lengthAdjust="spacing">FOR YOUR SCREENING MAMMOGRAM</text>

    <!-- badge -->
    <circle cx="1100" cy="560" r="117" fill="var(--pink)"/>
    <circle cx="1100" cy="560" r="111" fill="var(--white)"/>
    <circle cx="1100" cy="560" r="100" fill="none" stroke="var(--pink)" stroke-width="3"/>
    <rect class="ribbon" role="img" aria-label="Pink awareness ribbon illustration" clip-path="url(#badgeInner)" x="1002" y="462" width="196" height="196" fill="url(#ribbonTone)"/>
    <text class="badge-text" font-size="30" x="1117" y="523" text-anchor="middle">EARLY</text>
    <text class="badge-small" font-size="15" x="1117" y="538" text-anchor="middle">DETECTION</text>
    <text class="badge-text" font-size="30" x="1125" y="563" text-anchor="middle">SAVES</text>
    <text class="badge-text" font-size="30" x="1131" y="587" text-anchor="middle">LIVES</text>

    <!-- call to action pill -->
    <rect x="61" y="697" width="1169" height="63" rx="30" fill="var(--white)"/>
    <text class="cta-text" font-size="41" x="87" y="741" textLength="1116" lengthAdjust="spacing">TO BOOK AN APPOINTMENT, <tspan class="cta-strong">CALL 555-014-2290 ext. 1180</tspan></text>

    <text class="band-text" font-size="37" x="297" y="813" textLength="698" lengthAdjust="spacing"><tspan class="band-strong">SAME DAY</tspan> APPOINTMENTS <tspan class="band-strong">AVAILABLE!</tspan></text>

    <!-- footer contacts -->
    <path d="M58 858 a8 8 0 0 1 16 0 c0 7 -8 16 -8 16 s-8 -9 -8 -16 Z M66 855 a3 3 0 1 0 0.01 0 Z" fill="var(--white)" fill-rule="evenodd"/>
    <text class="footer-text" font-size="23" x="92" y="873" textLength="473" lengthAdjust="spacing">410 Harrow Lane, Maple City, Ontario A1B 2C3</text>
    <line x1="621" y1="851" x2="621" y2="883" stroke="var(--white)" stroke-width="2"/>
    <rect x="677" y="861" width="14" height="10" fill="none" stroke="var(--white)" stroke-width="1.8"/>
    <path d="M677 861 L684 867 L691 861" fill="none" stroke="var(--white)" stroke-width="1.5"/>
    <text class="footer-text" font-size="23" x="705" y="873" textLength="175" lengthAdjust="spacingAndGlyphs">imaging@lehn.example</text>
    <line x1="935" y1="851" x2="935" y2="883" stroke="var(--white)" stroke-width="2"/>
    <g fill="none" stroke="var(--white)" stroke-width="1.5">
      <circle cx="980" cy="866" r="7"/>
      <ellipse cx="980" cy="866" rx="3" ry="7"/>
      <line x1="973" y1="866" x2="987" y2="866"/>
    </g>
    <text class="footer-text" font-size="23" x="1002" y="873" textLength="212" lengthAdjust="spacingAndGlyphs">www.lehn.example/imaging</text>
  </svg>
</div>
</body>
</html>
```